Breezeway Comfort business cards design

Need a business card design for a Heating and Air Conditioning business. I need these items included.
Business name: Breezeway Comfort
Owner: Marcus Tollefsen
License # 2874590
Phone number # 555-382-4071
Email: breezewaycomfortair@mailvista.example
Sales
Service
Installation
Maintenance

Heating and Air Conditioning

Requirements
Must have
• Company name , license number , phone number , email

```html
<!DOCTYPE html>
<html lang="en">
<head>
<meta charset="utf-8">
<title>Breezeway Comfort — Business Cards</title>
<link rel="stylesheet" href="https://fonts.googleapis.com/css2?family=Exo+2:wght@400;500;700&display=swap">
<style>
  :root {
    --brand-blue: #1f45a3;
    --band-blue: #1d44a8;
    --brand-orange: #f07a26;
    --ink-blue: #1f3f95;
    --paper: #ffffff;
    --backdrop: #e9ebef;
  }
  * { margin: 0; padding: 0; box-sizing: border-box; }
  html, body {
    width: 1200px; height: 880px; overflow: hidden;
    background: var(--backdrop);
    font-family: "Exo 2", sans-serif;
  }
  .canvas { position: relative; width: 1200px; height: 880px; }

  .card {
    position: absolute; left: 260px; width: 680px; height: 388px;
    border-radius: 22px; overflow: hidden;
    box-shadow: 0 8px 24px rgba(20, 30, 60, 0.18);
  }

  /* Front */
  .card--front { top: 36px; background: var(--brand-blue); color: var(--paper); }
  .card--front .brand-name {
    position: absolute; left: 0; right: 0; top: 140px;
    text-align: center; font-weight: 700; font-size: 54px; letter-spacing: 1px;
    color: var(--paper);
  }
  .card--front .services {
    position: absolute; left: 0; right: 0; top: 250px;
    text-align: center; font-weight: 400; font-size: 21px; letter-spacing: 0.5px;
  }

  /* Back */
  .card--back { top: 456px; background: var(--paper); }
  .card--back .brand-name {
    position: absolute; left: 70px; top: 56px;
    font-weight: 700; font-size: 44px; letter-spacing: 1px; color: var(--ink-blue);
  }
  .card--back .accent-dot {
    position: absolute; left: -22px; top: 196px;
    width: 44px; height: 44px; border-radius: 50%; background: var(--brand-orange);
  }
  .person { position: absolute; left: 70px; top: 150px; }
  .person__name { font-weight: 700; font-size: 31px; color: var(--ink-blue); }
  .person__role { font-weight: 400; font-size: 19px; color: var(--brand-orange); margin-top: 2px; }
  .contact { position: absolute; left: 70px; top: 236px; list-style: none; }
  .contact__item {
    display: flex; align-items: center; gap: 10px;
    font-size: 19px; color: var(--ink-blue); margin-bottom: 6px;
  }
  .contact__icon { width: 22px; height: 22px; flex: none; }
  .license {
    position: absolute; right: 40px; top: 180px;
    font-size: 19px; color: var(--ink-blue);
  }
  .band {
    position: absolute; left: 0; right: 0; bottom: 0; height: 44px;
    background: var(--band-blue); color: var(--paper);
    display: flex; align-items: center; justify-content: center;
    font-size: 20px; letter-spacing: 0.5px;
  }
</style>
</head>
<body>
<main class="canvas">
  <section class="card card--front" aria-label="Card front">
    <div class="brand-name">Breezeway Comfort</div>
    <p class="services">Sales | Service | Installation | Maintenance</p>
  </section>

  <section class="card card--back" aria-label="Card back">
    <span class="accent-dot"></span>
    <div class="brand-name">Breezeway Comfort</div>
    <div class="person">
      <div class="person__name">Marcus Tollefsen</div>
      <div class="person__role">Business Advisor</div>
    </div>
    <p class="license">License # 2874590</p>
    <ul class="contact">
      <li class="contact__item">
        <svg class="contact__icon" viewBox="0 0 22 22" aria-hidden="true">
          <circle cx="11" cy="11" r="11" fill="#f07a26"/>
          <path d="M7 6.5c.6-.6 1.4-.6 1.8 0l1 1.5c.3.5.2 1-.2 1.4l-.6.5c.6 1.3 1.6 2.3 2.9 2.9l.5-.6c.4-.4.9-.5 1.4-.2l1.5 1c.6.4.6 1.2 0 1.8l-.7.7c-.8.8-2.5.5-4.6-1.2-1.8-1.5-3.4-3.6-3.6-5.2-.1-.9.1-1.8.6-2.6z" fill="#fff"/>
        </svg>
        555-382-4071
      </li>
      <li class="contact__item">
        <svg class="contact__icon" viewBox="0 0 22 22" aria-hidden="true">
          <circle cx="11" cy="11" r="11" fill="#f07a26"/>
          <rect x="5.5" y="7" width="11" height="8" rx="1" fill="#fff"/>
          <path d="M5.8 7.4 11 11.5l5.2-4.1" fill="none" stroke="#f07a26" stroke-width="1.2"/>
        </svg>
        breezewaycomfortair@mailvista.example
      </li>
    </ul>
    <div class="band">Sales | Service | Installation | Maintenance</div>
  </section>
</main>
</body>
</html>
```